we need a business card design for a professional painting business. This company has been up and going for about ten years. However it needs an new logo. we want this business card to be modern eye catching and easy to read. I currently have been looking for VP logos but can not find one that suits our needs. This Design should be Our start to a new beginning.
Industry/Entity Type
Painting
Contact Information for Business Card
Varesko Painting Inc.
Licensed & Insured
Tomas Varesko
Phone(631)384-4562
Fax (555) 846-3021
E-mail vareskopaintinginc@mailorbit.test
Requirements
Must have
- a new logo with  VP and i would like it to be in black and white.
i would also like the front to be a solid black with the logo only and then the back to have the information.

```html
<!DOCTYPE html>
<html lang="en">
<head>
<meta charset="utf-8">
<title>Varesko Painting Inc. — Business Card</title>
<link rel="stylesheet" href="https://fonts.googleapis.com/css2?family=PT+Sans+Narrow:wght@400;700&display=swap">
<style>
  :root {
    --backdrop: #e9e6e1;
    --card-black: #0e0e0e;
    --card-black-hi: #2a2a2a;
    --card-white: #fafafa;
    --card-white-lo: #e4e4e4;
    --ink: #2b2b2b;
    --ink-soft: #6a6a6a;
    --rule: #9a9a9a;
    --paper-text: #ffffff;
  }
  * { margin: 0; padding: 0; box-sizing: border-box; }
  html, body { width: 704px; height: 1200px; overflow: hidden; }
  body {
    background: var(--backdrop);
    font-family: "PT Sans Narrow", "Arial Narrow", sans-serif;
    position: relative;
  }
  .card {
    position: absolute;
    left: 72px;
    width: 560px;
    height: 320px;
    border-radius: 4px;
    box-shadow: 0 6px 18px rgba(0,0,0,0.25);
    overflow: hidden;
  }
  .card--front { top: 140px; background: linear-gradient(160deg, var(--card-black-hi) 0%, var(--card-black) 45%, #000 100%); }
  .card--back  { top: 740px; background: linear-gradient(160deg, var(--card-white) 0%, #f1f1f1 60%, var(--card-white-lo) 100%); }

  .brand { position: absolute; display: flex; align-items: center; gap: 14px; }
  .brand__mark { border-radius: 50%; flex: none; }
  .brand__name { font-weight: 700; line-height: 1; white-space: nowrap; }
  .brand__tagline { font-weight: 400; line-height: 1; margin-top: 6px; }

  .card--front .brand { left: 70px; top: 118px; }
  .card--front .brand__mark { width: 76px; height: 76px; background: var(--paper-text); }
  .card--front .brand__name { font-size: 40px; color: var(--paper-text); }
  .card--front .brand__tagline { font-size: 20px; color: var(--paper-text); }

  .card--back .brand { left: 28px; top: 62px; gap: 10px; }
  .card--back .brand__mark { width: 52px; height: 52px; background: var(--ink); }
  .card--back .brand__name { font-size: 26px; color: var(--ink); }
  .card--back .brand__tagline { font-size: 14px; color: var(--ink-soft); }

  .holder {
    position: absolute; left: 30px; top: 214px;
    font-size: 20px; color: var(--ink);
  }
  .holder-rule { position: absolute; left: 28px; top: 244px; width: 270px; height: 1px; background: var(--rule); }
  .divider { position: absolute; left: 322px; top: 40px; width: 1px; height: 240px; background: var(--rule); }

  .contact {
    position: absolute; right: 28px; top: 40px;
    list-style: none; text-align: right;
    font-size: 16px; color: var(--ink);
  }
  .contact li { display: flex; justify-content: flex-end; align-items: center; gap: 8px; height: 24px; }
  .contact svg { width: 14px; height: 14px; fill: var(--ink); }
  .contact__email { position: absolute; right: 28px; bottom: 36px; font-size: 16px; color: var(--ink); }
</style>
</head>
<body>
  <section class="card card--front" aria-label="Business card front">
    <div class="brand">
      <span class="brand__mark"></span>
      <div>
        <div class="brand__name">Varesko Painting Inc.</div>
        <div class="brand__tagline">Licensed &amp; Insured</div>
      </div>
    </div>
  </section>

  <section class="card card--back" aria-label="Business card back">
    <div class="brand">
      <span class="brand__mark"></span>
      <div>
        <div class="brand__name">Varesko Painting Inc.</div>
        <div class="brand__tagline">Licensed &amp; Insured</div>
      </div>
    </div>
    <p class="holder">Tomas Varesko</p>
    <span class="holder-rule"></span>
    <span class="divider"></span>
    <ul class="contact">
      <li>(555)217-9083
        <svg viewBox="0 0 16 16" aria-label="Phone"><path d="M3 1h3l1.5 4-2 1.2a9 9 0 0 0 4.3 4.3L11 8.5l4 1.5v3a2 2 0 0 1-2 2A13 13 0 0 1 1 3a2 2 0 0 1 2-2z"/></svg>
      </li>
      <li>(555) 846-3021 Fx
        <svg viewBox="0 0 16 16" aria-label="Fax"><path d="M4 1h7v4H4zM1 6h14v7h-3v2H4v-2H1zM5 10v4h6v-4z"/></svg>
      </li>
    </ul>
    <p class="contact__email">vareskopaintinginc@mailorbit.test</p>
  </section>
</body>
</html>
```